Bright and vibrant Jewelry Designer Web Page

Hi creative artists,

My name is Marta, I'm a local jewelry designer with a small store in Duesseldorf Germany. All my Jewelrys are unique and hand crafted by my self.

My designs are colorful, young, modern and trendy as well as timeless and durable due to the high quality materials. I use gold, silver, jewelry, fresh water pearls and hand crafted glass.

Competitors are local goldsmith which produce custom-made jewelry.

I have started my business with my jewelry label "twigs and ribbons" 2007:
http://www.twigs-and-ribbons.de/start.php

In 2009 I have opened my store "Kupfer und Leinen" (silver and silk) together with a fashion designer:
http://www.kupfer-leinen.de/home.php
https://www.facebook.com/Kupfer.und.Leinen (latest jewelrys)

Scope of pages:
● welcome page
● category overview
- short introduction
- sub categories: Earring, Necklace, Ring, Bride Jewelry, ...
● category page
- short introduction
- products of this category
● product page
- short introduction
- about 3 to 4 pictures
- description: materials, dimensions
- price
- ! important ! related products
● contact page
- address
- contact form
● blog
- picture
- text

Conclusion:
● We need a emotional page
● Lots of impressive and brilliant product images
● A feminine touch
● Last but not least the design should reflect
- outstanding design
- uniqueness
- made-to-measure

Target Market(s)

Women in the mid 20's and 30's , interested in individual style, fashion and luxury goods

Industry/Entity Type

Jewelry

Requirements
Must have
• ● css for screen, mobile devices and print
● full function also with out JavaScript
● only use free available fonts e.g. Lumora Type Library (http://www.lumoratype.example/webfonts)
Should not have
• ● sound
● flash

```html
<!DOCTYPE html>
<html lang="en">
<head>
<meta charset="utf-8">
<title>Jewelry – the best online store</title>
<link rel="stylesheet" href="https://fonts.googleapis.com/css2?family=Gelasio:ital,wght@0,400;0,700;1,700&family=Arimo:wght@400;700&display=swap">
<style>
:root{
  --topbar:#1e1b1a;
  --topbar-text:#e8e2dc;
  --nav-active:#f3b99a;
  --pink-light:#f8c2b4;
  --pink-mid:#f19b88;
  --headline-white:#ffffff;
  --headline-rust:#c25a45;
  --cream:#fbf8ec;
  --heading-brown:#8b6a55;
  --teal:#3e9bb0;
  --salmon:#f0a08c;
  --text:#333;
  --link-text:#a4623f;
  --price:#2a2220;
  --frame:#e4dccb;
  --footer:#7b5a47;
  --footer-text:#f4ebe2;
}
*{margin:0;padding:0;box-sizing:border-box}
html,body{width:900px;height:1200px;overflow:hidden}
body{position:relative;background:var(--cream);font-family:"Arimo",Arial,sans-serif;color:var(--text)}
.abs{position:absolute}

.topbar{left:0;top:0;width:900px;height:21px;background:var(--topbar);font-size:10px}
.topnav{left:142px;top:0;display:flex;height:21px}
.topnav a{display:block;padding:0 10px;line-height:21px;color:var(--topbar-text);text-decoration:none;font-family:"Gelasio",Georgia,serif;font-size:10px;border-right:1px solid #3a3533}
.topnav a.active{color:var(--nav-active)}
.welcome{right:108px;top:5px;color:var(--topbar-text);font-size:9px}
.welcome u{color:var(--nav-active)}
.welcome b{color:#fff}

.hero{left:0;top:21px;width:900px;height:334px;background:linear-gradient(90deg,var(--pink-mid),var(--pink-light) 30%,var(--pink-light) 70%,var(--pink-mid))}
.brand{left:142px;top:36px;font-family:"Gelasio",Georgia,serif;font-weight:700;font-size:29px;line-height:36px;color:#2b2522;white-space:nowrap}
.tagline{left:262px;top:61px;font-size:8px;color:#7a4a3c;white-space:nowrap}
.cartline{left:747px;top:34px;font-size:8px;color:#333}
.search{left:607px;top:50px;font-size:8px;font-weight:700;color:#7a4a3c;display:flex;align-items:center;gap:6px}
.search span.field{display:block;width:128px;height:15px;background:#fff}
.search span.go{display:block;width:21px;height:15px;background:var(--teal);color:#fff;font-weight:400;text-align:center;line-height:15px}
.model{left:445px;top:90px;width:315px;height:265px;background:linear-gradient(135deg,#f3d1b5,#e9b594 60%,#d99c80)}
.headline{left:198px;top:134px;font-family:"Gelasio",Georgia,serif;font-style:italic;font-weight:700;color:var(--headline-white);font-size:45px;white-space:nowrap}
.sub{left:198px;top:198px;font-family:"Gelasio",Georgia,serif;font-style:italic;font-weight:700;color:var(--headline-rust);font-size:25px;line-height:31px;white-space:nowrap}
.arrow{width:52px;height:58px;top:183px}

.sidebar h2{font-family:"Gelasio",Georgia,serif;font-weight:700;color:var(--heading-brown);font-size:16px;white-space:nowrap}
.catlist{left:163px;top:413px;list-style:none;font-size:10px;color:#5b4a40}
.catlist li{height:19.4px;display:flex;align-items:center;gap:4px;white-space:nowrap}
.catlist li::before{content:"";width:5px;height:5px;border-radius:50%;background:var(--teal)}
.plus{left:152px;top:437px;width:8px;height:8px;border:1px solid #999;font-size:8px;line-height:6px;text-align:center;color:#666}

.cartbox{left:142px;top:628px;width:152px;height:184px;background:#fff;border:1px solid #eee2d3;border-radius:4px}
.cartbox h2{position:absolute;left:18px;top:18px}
.cartbox .row{position:absolute;left:19px;width:112px;height:14px;border:1px solid #e8e2d6;font-size:8px;color:#8a6e5a;padding:0 3px;display:flex;justify-content:space-between;align-items:center}
.cartbox p{position:absolute;left:19px;font-size:9px;color:#333;white-space:nowrap}
.btn{position:absolute;top:137px;height:17px;border-radius:9px;color:#fff;font-size:8px;text-align:center;line-height:17px}

.select{left:161px;top:877px;width:113px;height:15px;background:#fff;border:1px solid #ccc;font-size:8px;color:#555;padding-left:4px;line-height:13px}
.select i{position:absolute;right:1px;top:1px;width:11px;height:11px;background:#ddd;border:1px solid #888}

.product{width:112px}
.frame{width:112px;height:151px;background:#fff;border:1px solid var(--frame);border-radius:6px;padding:8px}
.photo{width:100%;height:100%;background:radial-gradient(circle,#e6e6e8,#ffffff 70%)}
.pname{margin-top:13px;height:28px;font-size:7.4px;line-height:12px;color:var(--link-text);width:114px;overflow:hidden}
.price{margin-top:5px;font-family:"Gelasio",Georgia,serif;font-style:italic;font-weight:700;font-size:17px;color:var(--price)}
.view{margin-top:2px;font-size:8px;color:var(--teal);text-decoration:underline;display:flex;align-items:center;gap:4px}
.view::before{content:"";width:6px;height:6px;border-radius:50%;background:var(--salmon)}

.footer{left:0;top:1145px;width:900px;height:55px;background:var(--footer);color:var(--footer-text);font-size:9px}
.footlinks{left:142px;top:22px;display:flex;gap:14px}
.copy{left:142px;top:38px;font-size:8px}
.currency{left:630px;top:22px;display:flex;align-items:center;gap:4px;font-size:8px}
.flag{width:11px;height:8px}
.cur{width:62px;height:14px;background:#fff;color:#333;padding-left:3px;line-height:14px;position:relative}
.cur i{position:absolute;right:1px;top:1px;width:11px;height:11px;background:#ddd}
</style>
</head>
<body>

<div class="abs topbar">
  <nav class="abs topnav"><a class="active">HOME</a><a>SPECIALS</a><a>SITEMAP</a><a>CONTACT</a></nav>
  <div class="abs welcome">Welcome, ( <u>Log in</u> ) &nbsp;<b>Your Account</b></div>
</div>

<header class="abs hero"></header>
<div class="abs brand">Jewelry</div>
<div class="abs tagline">the best online store</div>
<div class="abs cartline"><b>Cart:</b> (empty)</div>
<div class="abs search">Search <span class="field"></span><span class="go">Go</span></div>
<div class="abs model" role="img" aria-label="Smiling blonde woman wearing earrings and a pearl necklace"></div>
<div class="abs headline">Clearance</div>
<div class="abs sub">save up to 70% off+<br>up to an extra 40%<br>online &amp; 10% in store</div>
<svg class="abs arrow" style="left:126px" viewBox="0 0 52 58"><ellipse cx="26" cy="29" rx="26" ry="29" fill="#fde6de"/><path d="M31 19 L21 29 L31 39" stroke="#8e3f30" stroke-width="6" fill="none"/></svg>
<svg class="abs arrow" style="left:756px" viewBox="0 0 52 58"><ellipse cx="26" cy="29" rx="26" ry="29" fill="#fde6de"/><path d="M21 19 L31 29 L21 39" stroke="#8e3f30" stroke-width="6" fill="none"/></svg>

<aside class="sidebar">
  <h2 class="abs" style="left:161px;top:383px">Categories</h2>
  <div class="abs plus">+</div>
  <ul class="abs catlist">
    <li>Diamond Rings</li><li>Earrings</li><li>Pendants</li><li>Journey Jewelry</li><li>Pins and Brooches</li>
    <li>Family Jewelry</li><li>Men's Jewelry</li><li>Men's Gifts</li><li>Bracelets</li><li>Religious Jewelry</li>
  </ul>
  <div class="abs cartbox">
    <h2>Cart <small style="font-size:8px">&#9650;</small></h2>
    <p style="top:47px">No products</p>
    <div class="row" style="top:61px"><span>Shipping</span><span>$0.00</span></div>
    <div class="row" style="top:85px"><span>Total</span><span>$0.00</span></div>
    <p style="top:113px">Prices are tax excluded</p>
    <span class="btn" style="left:19px;width:42px;background:var(--teal)">Cart</span>
    <span class="btn" style="left:65px;width:64px;background:var(--salmon)">Check out</span>
  </div>
  <h2 class="abs" style="left:161px;top:841px">Manufacturers</h2>
  <div class="abs select">All manufacturers<i></i></div>
</aside>

<main>
  <div class="abs product" style="left:308px;top:387px"><div class="frame"><div class="photo" role="img" aria-label="Diamond framed engagement ring"></div></div><div class="pname">1 CT. T.W. Diamond Framed Engagement Ring in 14K White</div><div class="price">$549.00</div><div class="view">view</div></div>
  <div class="abs product" style="left:432px;top:387px"><div class="frame"><div class="photo" role="img" aria-label="Princess-cut diamond engagement ring"></div></div><div class="pname">1-1/2 CT. T.W. Princess-Cut Diamond Engagement Ring...</div><div class="price">$215.00</div><div class="view">view</div></div>
  <div class="abs product" style="left:557px;top:387px"><div class="frame"><div class="photo" role="img" aria-label="Seven-stone diamond band"></div></div><div class="pname">1/5 CT. T.W. Diamond<br>Seven-Stone Band in 14K White</div><div class="price">$379.95</div><div class="view">view</div></div>
  <div class="abs product" style="left:681px;top:387px"><div class="frame"><div class="photo" role="img" aria-label="Square diamond stud earrings"></div></div><div class="pname">1/8 CT. T.W. Diamond Square Composite Stud Earrings</div><div class="price">$315.00</div><div class="view">view</div></div>

  <div class="abs product" style="left:308px;top:636px"><div class="frame"><div class="photo" role="img" aria-label="Diamond knot earrings"></div></div><div class="pname">1/4 CT. T.W. Diamond Knot<br>Earrings in Sterling Silver</div><div class="price">$270.00</div><div class="view">view</div></div>
  <div class="abs product" style="left:432px;top:636px"><div class="frame"><div class="photo" role="img" aria-label="Round diamond accent pendant"></div></div><div class="pname">Diamond Accent Round Pendant<br>in Sterling Silver and...</div><div class="price">$620.00</div><div class="view">view</div></div>
  <div class="abs product" style="left:557px;top:636px"><div class="frame"><div class="photo" role="img" aria-label="Double heart diamond pendant"></div></div><div class="pname">1/4 CT. T.W. Diamond Double Heart Pendant in...</div><div class="price">$345.00</div><div class="view">view</div></div>
  <div class="abs product" style="left:681px;top:636px"><div class="frame"><div class="photo" role="img" aria-label="Black and white diamond teardrop pendant"></div></div><div class="pname">3/4 CT. T.W. Enhanced Black and White Diamond...</div><div class="price">$549.00</div><div class="view">view</div></div>

  <div class="abs product" style="left:308px;top:885px"><div class="frame"><div class="photo" role="img" aria-label="Diamond flower necklace"></div></div><div class="pname">Diamond Accent Flower<br>Necklace in Sterling Silver</div><div class="price">$215.00</div><div class="view">view</div></div>
  <div class="abs product" style="left:432px;top:885px"><div class="frame"><div class="photo" role="img" aria-label="Infinity diamond pendant"></div></div><div class="pname">1 CT. T.W. Diamond Framed Engagement Ring in 14K White</div><div class="price">$518.00</div><div class="view">view</div></div>
  <div class="abs product" style="left:557px;top:885px"><div class="frame"><div class="photo" role="img" aria-label="Cushion-cut blue topaz ring"></div></div><div class="pname">Cushion-Cut Blue Topaz Fashion<br>Ring in Sterling...</div><div class="price">$315.00</div><div class="view">view</div></div>
  <div class="abs product" style="left:681px;top:885px"><div class="frame"><div class="photo" role="img" aria-label="Sapphire and diamond ring"></div></div><div class="pname">Sapphire and 1/2 CT. T.W. Diamond Ring in 14K White...</div><div class="price">$270.00</div><div class="view">view</div></div>
</main>

<footer class="abs footer">
  <div class="abs footlinks"><span>Specials</span><span>New products</span><span>Top sellers</span><span>About us</span><span>Contact us</span></div>
  <div class="abs copy">©2011 Powered by ShopForge™. All rights reserved</div>
  <div class="abs currency">
    <svg class="flag" viewBox="0 0 11 8"><rect width="11" height="8" fill="#2b3f8c"/><path d="M0 0L11 8M11 0L0 8" stroke="#fff" stroke-width="1.5"/><path d="M5.5 0V8M0 4H11" stroke="#c8202e" stroke-width="2"/></svg>
    <svg class="flag" viewBox="0 0 11 8"><rect width="4" height="8" fill="#2b3f8c"/><rect x="4" width="3" height="8" fill="#fff"/><rect x="7" width="4" height="8" fill="#c8202e"/></svg>
    <svg class="flag" viewBox="0 0 11 8"><rect width="11" height="8" fill="#c8202e"/><rect y="2" width="11" height="4" fill="#f0c020"/></svg>
    <span style="margin-left:8px">Currency:</span><span class="cur">Dollar<i></i></span>
  </div>
</footer>

</body>
</html>
```